We are creating the packaging for our premium gift box: “Sunward Links Reserve.”
This box contains a green fee for two people, valid at the recipient’s choice of one of the most exclusive and scenic golf courses in Italy.
• Box dimensions: 16x16 x 2 cm
• Label coverage: The design must wrap around the two large square sides and the two lateral edges, similar to Gleamcase packaging.
• Style: Elegant, refined, and modern.

Front design:
• A strong emotional golf image (luxury golf course setting, Italian landscape, or moment of play).
• Title: “Sunward Links Reserve”.
• It must be clearly visible that the box includes a round of golf for two people in one of the 50 most exclusive and scenic golf courses in Italy.

Back design:
The back should contain the following text:

Discover Italy’s most iconic golf courses
With this gift box you and a guest can enjoy a round of golf at your choice of one of the 20 most beautiful courses in Italy. From championship layouts to breathtaking landscapes, every round is an unforgettable experience.

Some of the included courses:
• Tessa Varnelli Golf Club, Rome (host of the Halvern Trophy 2023)
• Grand Bosco Le Fontane, Turin
• Calmora Resort, Sicily
• Circolo Golf Villa Brunetta, Lake Como
• Lunaro Golf Club, Costa Smeralda
• Belvedrano Golf Club, Tuscany
• Golf Club Montefrassino, Piedmont

…and many more top-ranked Italian destinations.

How it works:
1. Choose your preferred golf course from the list.
2. Book directly with the club, using the code provided inside the box.
3. Enjoy an exclusive round of golf for two people.

This gift box offers flexibility, freedom, and access to Sunward Links Reserve experiences — the perfect present for any passionate golfer.

The overall design should capture the prestige of Italian golf and communicate that this is the most desired gift for golf lovers.

Target Market(s)

Our target market is golf enthusiasts, gift buyers, and people looking for premium experience gifts. The typical buyer is between 30–60 years old, often purchasing for friends, family, or business partners. The gift should feel aspirational, elegant, and special — the perfect present for any golfer.

Industry/Entity Type

Gift boxes and experience packages, with a specific focus on golf and premium leisure experiences.

Font styles to use
Serif

Requirements
Must have
• A premium, elegant box design (21x21x2 cm) in line with luxury gift standards. • Emotional, high-quality golf imagery that immediately conveys the excitement of playing golf. • Clear and stylish branding of TeeParcel. • A design style inspired by Gleamcase (label wrapping front + two sides + back). • On the back: a list of included golf courses and simple instructions on how to use the gift box.
Nice to have
• Minimalist and modern style with clean lines. • Touches of copper or metallic accents for a premium feel. • A contemporary design aesthetic similar to Nook Drive or Parvenda. • Lifestyle imagery that conveys joy, elegance, and aspiration, not just golf action.
Should not have
• No cheap or cluttered visuals. • No heavy use of gold or champagne tones (avoid cliché luxury). • No cartoonish or overly playful styles. • No complex text-heavy design — clarity and elegance are key.

```html
<!DOCTYPE html>
<html lang="en">
<head>
<meta charset="utf-8">
<title>Sunward Links Reserve – Gift Box Label</title>
<link href="https://fonts.googleapis.com/css2?family=Cinzel:wght@400&family=Playfair+Display:wght@400&display=swap" rel="stylesheet">
<style>
  :root {
    --page: #f1f1f1;
    --forest: #1b3629;
    --forest-mid: #2c5230;
    --gold: #d8b13a;
    --gold-light: #f4da6a;
    --gold-deep: #9a7518;
    --sun: #fff6c8;
    --field: #c9a232;
    --ball: rgba(120, 140, 60, 0.14);
  }
  * { box-sizing: border-box; margin: 0; padding: 0; }
  html, body {
    width: 1200px; height: 630px; overflow: hidden;
    background: var(--page);
  }
  .canvas { position: relative; width: 1200px; height: 630px; }

  .panel {
    position: absolute; top: 28px; width: 552px; height: 559px;
    background: var(--forest);
  }
  .panel--front { left: 30px; }
  .panel--back { left: 617px; }

  .frame {
    position: absolute; left: 26px; top: 33px; width: 502px; height: 501px;
    border: 4px solid var(--gold);
    border-image: linear-gradient(135deg, var(--gold-deep), var(--gold-light) 30%, var(--gold) 60%, var(--gold-deep)) 1;
    overflow: hidden;
  }

  .hero-art {
    position: absolute; inset: 0;
    background:
      radial-gradient(circle 110px at 63% 62%, var(--sun) 0, rgba(255,240,170,0.75) 25%, rgba(240,200,70,0) 100%),
      linear-gradient(180deg, var(--forest) 0%, var(--forest) 34%, var(--forest-mid) 46%, #8e9a2a 58%, #e6c445 70%, var(--field) 82%, #a8862a 100%);
  }

  .gold-title {
    font-family: "Cinzel", serif; font-weight: 400;
    text-align: center; text-transform: uppercase;
    color: var(--gold-light);
  }
  .front-title {
    position: absolute; left: 0; right: 0; top: 40px;
    font-size: 44px; line-height: 54px; letter-spacing: 2px;
  }
  .front-tagline {
    position: absolute; left: 0; right: 0; top: 166px; text-align: center;
    font-family: "Playfair Display", serif; color: var(--gold);
  }
  .front-tagline .lead { font-size: 17px; line-height: 24px; }
  .front-tagline .sub { font-size: 14px; line-height: 22px; }

  .ball-mark {
    position: absolute; left: 262px; top: 174px; width: 228px; height: 228px;
    border-radius: 50%; background: var(--ball);
  }
  .back-title {
    position: absolute; left: 0; right: 0; top: 22px;
    font-size: 30px; line-height: 34px; letter-spacing: 1px;
  }
  .back-content {
    position: absolute; left: 25px; width: 452px;
    font-family: "Playfair Display", serif; font-weight: 400; color: var(--gold);
  }
  .section-heading {
    font-family: "Cinzel", serif; font-weight: 400;
    text-align: center; text-transform: uppercase; letter-spacing: 1px;
  }
  .intro-heading { top: 100px; font-size: 15px; line-height: 18px; }
  .intro { top: 120px; font-size: 12px; line-height: 14px; text-align: justify; }
  .course-list { top: 181px; font-size: 12px; line-height: 14px; }
  .course-list ul { list-style: none; }
  .course-list li::before { content: "• "; }
  .more { top: 305px; font-size: 12px; line-height: 14px; }
  .how-heading { top: 336px; font-size: 15px; line-height: 18px; }

  .step {
    position: absolute; top: 381px; width: 150px; text-align: center;
    font-family: "Playfair Display", serif; color: var(--gold);
  }
  .step--choose { left: 19px; }
  .step--book { left: 172px; }
  .step--enjoy { left: 333px; }
  .step-icon { height: 54px; display: flex; justify-content: center; align-items: flex-end; }
  .step-text { font-size: 10px; line-height: 13px; margin-top: 14px; }
  .player-icon { width: 62px; height: 44px; background: rgba(216,177,58,0.35); border-radius: 3px; }
</style>
</head>
<body>
<main class="canvas">

  <section class="panel panel--front">
    <div class="frame">
      <div class="hero-art" role="img" aria-label="Golfer mid-swing on a sunlit Italian course at sunset, trees and a pond in the valley"></div>
      <h1 class="gold-title front-title">Sunward Links<br>Reserve.</h1>
      <div class="front-tagline">
        <p class="lead">A Round Worth Remembering</p>
        <p class="sub">Play Where Legends Walk — Italy’s Top 50 Courses</p>
      </div>
    </div>
  </section>

  <section class="panel panel--back">
    <div class="frame">
      <div class="ball-mark" role="img" aria-label="Faint golf ball decoration"></div>
      <h2 class="gold-title back-title">Sunward Links<br>Reserve.</h2>

      <h3 class="back-content section-heading intro-heading">Discover Italy’s most iconic golf courses</h3>
      <p class="back-content intro">With this gift box you and a guest can enjoy a round of golf at your choice of one of the 20 most beautiful courses in Italy. From championship layouts to breathtaking landscapes, every round is an unforgettable experience.</p>

      <div class="back-content course-list">
        <p>Some of the included courses:</p>
        <ul>
          <li>Tessa Varnelli Golf Club, Rome (host of the Halvern Trophy 2023)</li>
          <li>Grand Bosco Le Fontane, Turin</li>
          <li>Calmora Resort, Sicily</li>
          <li>Circolo Golf Villa Brunetta, Lake Como</li>
          <li>Lunaro Golf Club, Costa Smeralda</li>
          <li>Belvedrano Golf Club, Tuscany</li>
          <li>Golf Club Montefrassino, Piedmont</li>
        </ul>
      </div>
      <p class="back-content more">…and many more top-ranked Italian destinations.</p>

      <h3 class="back-content section-heading how-heading">How it works:</h3>

      <div class="step step--choose">
        <div class="step-icon">
          <svg width="42" height="52" viewBox="0 0 42 52" fill="none" stroke="var(--gold)" stroke-width="1.4">
            <path d="M1 1 H41 V40 L30 51 H1 Z"/>
            <path d="M30 51 V40 H41"/>
            <path d="M6 11 l2.5 3 l4 -5 M6 21 l2.5 3 l4 -5 M6 31 l2.5 3 l4 -5"/>
            <path d="M16 11 H35 M16 21 H35 M16 31 H35"/>
          </svg>
        </div>
        <p class="step-text">Choose your preferred<br>golf course from the list.</p>
      </div>
      <div class="step step--book">
        <div class="step-icon">
          <svg width="42" height="52" viewBox="0 0 42 52" fill="none" stroke="var(--gold)" stroke-width="1.4">
            <rect x="1" y="1" width="40" height="50"/>
            <path d="M9 9 l1.6 3.4 l3.6 .4 l-2.7 2.4 l.8 3.6 l-3.3 -1.9 l-3.3 1.9 l.8 -3.6 l-2.7 -2.4 l3.6 -.4 Z"/>
            <path d="M4 24 H38"/>
            <text x="17" y="16" font-family="Cinzel, serif" font-size="7" fill="var(--gold)" stroke="none">CODE</text>
          </svg>
        </div>
        <p class="step-text">Book directly with the club, using<br>the code provided inside the box.</p>
      </div>
      <div class="step step--enjoy">
        <div class="step-icon">
          <div class="player-icon" role="img" aria-label="Icon of two golfers celebrating"></div>
        </div>
        <p class="step-text">Enjoy an exclusive round<br>of golf for two people.</p>
      </div>
    </div>
  </section>

</main>
</body>
</html>
```